Touring Cabaret Seasons Needs a Poster Design

We need a poster design for upcoming Cabaret seasons in Melbourne and Adelaide (Australia) for a prestigious festival.

Show is titled "Hold Still While I Tune My Ukulele..." and is a comedy parody of bad cabaret and deluded performers. We'd like the poster to reflect the comedy of the piece without being silly and inaccessable.

Artist has recently won awards for this show and these will need to be listed as a part of the design.

I have attached a couple of photographs that can be used - one is the artist with a blank book cover and these could be used to overlay text.

Would like it to not look too wordy, however I realise we've asked for a lot of text to be included.

Target Market(s)

Ages 20 - 40 cabaret or comedy fans.

Industry/Entity Type

Festival

Requirements
Must have
• TEXT:
The Velvet Lantern presents:
Hold Still While I Tune My Ukulele...

TEXT:
WINNER of BEST CABARET, BEST WRITING and PEOPLE’S CHOICE awards at Brisk + Bright Revue 2011

TEXT:
The Copper Kettle (Melbourne)
Feb 23rd to the 26th

El Faro, REVedge(Adelaide)
March 3rd and 4th

QUOTES:
“...the funniest things in spandex. 4.5 stars” – The Ledger on Dribble! A revue about handball.

“a clever dissection of bad cabaret” – Owen Marsh, The Ledger on Brisk + Bright Revue
Nice to have
• TEXT:
The last time someone showed you a little something they were working on, did you lose an hour of your life you will never get back? Don’t worry – we’ve all been there.

TEXT:
Composer and co-writer of Dribble! (A revue about handball) and WINNER of BEST CABARET, BEST WRITING and PEOPLE’S CHOICE awards at Brisk + Bright Revue 2011, presents her full show, with more original music and helpful anecdotes.

WEBSITE:
More info at www.pagebook.example/thevelvetlantern

```html
<!DOCTYPE html>
<html lang="en">
<head>
<meta charset="utf-8">
<title>Hold Still While I Tune My Ukulele... — The Velvet Lantern</title>
<link rel="stylesheet" href="https://fonts.googleapis.com/css2?family=Architects+Daughter&family=Londrina+Solid:wght@400;900&display=swap">
<style>
  :root {
    --page: #ffffff;
    --ink: #050505;
    --chalk: #f2f0ea;
    --chalk-dim: #cfccc4;
    --accent: #b3262a;
    --paper: #efece4;
    --paper-ink: #6a6660;
    --stage-warm: #5a3b22;
  }
  * { margin: 0; padding: 0; box-sizing: border-box; }
  html, body { width: 1200px; height: 800px; overflow: hidden; background: var(--page); }
  .poster {
    position: absolute; left: 323px; top: 7px; width: 554px; height: 786px;
    background: var(--ink); color: var(--chalk);
    font-family: "Architects Daughter", cursive;
    overflow: hidden;
  }
  .presenter {
    position: absolute; top: 28px; left: 0; width: 100%;
    text-align: center; font-size: 21px; letter-spacing: 1.5px;
  }
  .presenter-rule { position: absolute; left: 68px; top: 58px; }
  .title {
    position: absolute; top: 70px; left: 0; width: 100%;
    text-align: center; font-family: "Londrina Solid", sans-serif; font-weight: 900;
    font-size: 47px; line-height: 56px; color: var(--chalk);
    letter-spacing: 2.5px;
    -webkit-text-stroke: 1.5px #777;
  }
  .awards {
    position: absolute; top: 196px; left: 0; width: 100%;
    text-align: center; font-size: 15px; line-height: 19px;
  }
  .performer-photo {
    position: absolute; left: 17px; top: 372px; width: 330px; height: 318px;
    background: radial-gradient(ellipse at 45% 35%, var(--stage-warm) 0%, #2a1a10 40%, var(--ink) 75%);
  }
  .speech {
    position: absolute; left: 187px; top: 266px; width: 232px;
    background: var(--paper); color: var(--paper-ink);
    font-size: 10.5px; line-height: 13px; padding: 6px 10px 7px;
    font-style: italic;
    transform: rotate(-1deg);
  }
  .speech::after {
    content: ""; position: absolute; left: 22px; top: 100%;
    width: 22px; height: 20px; background: var(--paper);
    clip-path: polygon(0 0, 100% 0, 15% 100%);
  }
  .venue { position: absolute; text-align: center; font-size: 15px; line-height: 19px; }
  .venue svg { position: absolute; left: 0; top: 0; }
  .venue p { position: relative; }
  .venue-melbourne { left: 322px; top: 370px; width: 180px; height: 100px; padding-top: 18px; }
  .venue-adelaide { left: 326px; top: 456px; width: 190px; height: 104px; padding-top: 20px; }
  .quotes {
    position: absolute; left: 255px; top: 602px; width: 300px;
    text-align: center; font-size: 12px; line-height: 16px; color: var(--chalk-dim);
    white-space: nowrap;
  }
  .quotes blockquote + blockquote { margin-top: 12px; }
  .more-info {
    position: absolute; bottom: 22px; left: 0; width: 100%;
    text-align: center; font-size: 19px; letter-spacing: 0.5px;
  }
</style>
</head>
<body>
<main class="poster">
  <p class="presenter">THE VELVET LANTERN PRESENTS:</p>
  <svg class="presenter-rule" width="420" height="6" aria-hidden="true">
    <path d="M2 3 Q210 1 418 4" stroke="var(--accent)" stroke-width="1.5" fill="none"/>
  </svg>

  <h1 class="title">Hold Still While I<br>Tune My Ukulele...</h1>

  <p class="awards">WINNER of BEST CABARET, BEST WRITING and PEOPLES CHOICE awards<br>at Brisk + Bright Revue 2011</p>

  <div class="performer-photo" role="img" aria-label="Photograph of the performer singing on a dark stage in a black gown and gold gloves"></div>

  <p class="speech">The last time someone showed you a little something they were working on, did you lose an hour of your life you will never get back? Dont worry - weve all been there.</p>

  <div class="venue venue-melbourne">
    <svg width="180" height="100" aria-hidden="true">
      <ellipse cx="90" cy="50" rx="84" ry="44" stroke="var(--accent)" stroke-width="1.3" fill="none"/>
      <ellipse cx="92" cy="48" rx="88" ry="41" stroke="var(--accent)" stroke-width="1" fill="none" transform="rotate(-3 90 50)"/>
    </svg>
    <p>The Copper Kettle<br>(Melbourne)<br>Feb 23rd to the 26th</p>
  </div>

  <div class="venue venue-adelaide">
    <svg width="190" height="104" aria-hidden="true">
      <ellipse cx="95" cy="52" rx="89" ry="46" stroke="var(--accent)" stroke-width="1.3" fill="none"/>
      <ellipse cx="93" cy="50" rx="92" ry="43" stroke="var(--accent)" stroke-width="1" fill="none" transform="rotate(4 95 52)"/>
    </svg>
    <p>El Faro, REVedge<br>(Adelaide)<br>March 3rd and 4th</p>
  </div>

  <section class="quotes">
    <blockquote>“...the funniest things in spandex. 4.5 stars”<br>/The Ledger on Dribble! A revue about handball/</blockquote>
    <blockquote>“a clever dissection of bad cabaret”<br>/Owen Marsh, The Ledger on Brisk + Bright Revue/</blockquote>
  </section>

  <p class="more-info">More info at www.pagebook.example/thevelvetlantern</p>
</main>
</body>
</html>
```